Dunmore Ag Solutions, LLC

Sales, Service, and Repair of Grain Bins

Must include: Insured

Industry/Entity Type

Sales

Contact Information for Business Card

We would like the submitted file to be used in making the business card. Either shrinking it down to use as a "logo" in the left hand side or use it as a back drop with writing over top of it. Would like to have on card also is a name and number: Todd Dunmore (555) 268-0137

Font styles to use
Serif

Requirements
Must have
• Name of owner: Todd Dunmore phone number: 555 268 0137. Free estimates
Nice to have
• Simple and neat design, needs to have the word insured somewhere on the card

```html
<!DOCTYPE html>
<html lang="en">
<head>
<meta charset="utf-8">
<title>Dunmore Ag Solutions, LLC — Business Cards</title>
<link rel="stylesheet" href="https://fonts.googleapis.com/css2?family=Montserrat:wght@500;700;800&family=Open+Sans:wght@700&family=Roboto:wght@400&display=swap">
<style>
  :root {
    --backdrop: #bdbec0;
    --paper: #ffffff;
    --ink: #000000;
    --rule-light: #8a8a8a;
  }
  * { box-sizing: border-box; margin: 0; padding: 0; }
  html, body {
    width: 1200px; height: 1000px; overflow: hidden;
    background: var(--backdrop);
  }
  .stage { position: relative; width: 1200px; height: 1000px; }

  .card {
    position: absolute; left: 286px; width: 628px; height: 358px;
    background: var(--paper); color: var(--ink);
    --fg: var(--ink);
  }
  .card--light { top: 118px; }
  .card--dark { top: 524px; background: var(--ink); --fg: var(--paper); color: var(--paper); }

  .brand {
    position: absolute; left: 94px; top: 100px; width: 160px;
    font-family: "Montserrat", sans-serif; font-weight: 800;
    color: var(--fg); text-align: right; line-height: 1.05;
  }
  .brand__name { display: block; font-size: 40px; letter-spacing: -0.5px; }
  .brand__sub { display: block; font-size: 20px; margin-top: 4px; }
  .brand__llc { display: block; font-size: 14px; margin-top: 6px; }

  .divider {
    position: absolute; left: 315px; top: 35px; width: 1px; height: 224px;
    background: var(--fg); opacity: .75;
  }

  .contact { position: absolute; left: 356px; top: 110px; font-family: "Roboto", sans-serif; color: var(--fg); }
  .contact__name { font-size: 32px; line-height: 1; }
  .contact__phone { font-size: 23px; margin-top: 10px; letter-spacing: .3px; }

  .credential {
    position: absolute; left: 0; right: 0; top: 276px; text-align: center;
    font-family: "Open Sans", sans-serif; font-weight: 700; font-size: 18px; color: var(--fg);
  }
  .credential__rule {
    position: absolute; left: 203px; top: 300px; width: 226px; height: 1px;
    background: var(--fg); opacity: .8;
  }
  .services {
    position: absolute; left: 0; right: 0; top: 306px; text-align: center;
    font-family: "Montserrat", sans-serif; font-weight: 500; font-size: 15.5px; color: var(--fg);
  }
</style>
</head>
<body>
<main class="stage">
  <section class="card card--light">
    <div class="brand">
      <span class="brand__name">Dunmore</span>
      <span class="brand__sub">Ag Solutions</span>
      <span class="brand__llc">LLC</span>
    </div>
    <div class="divider"></div>
    <div class="contact">
      <p class="contact__name">Todd Dunmore</p>
      <p class="contact__phone">(555) 268-0137</p>
    </div>
    <p class="credential">Insured</p>
    <div class="credential__rule"></div>
    <p class="services">Sales • Service • and Repair of Grain Bins</p>
  </section>

  <section class="card card--dark">
    <div class="brand">
      <span class="brand__name">Dunmore</span>
      <span class="brand__sub">Ag Solutions</span>
      <span class="brand__llc">LLC</span>
    </div>
    <div class="divider"></div>
    <div class="contact">
      <p class="contact__name">Todd Dunmore</p>
      <p class="contact__phone">(555) 268-0137</p>
    </div>
    <p class="credential">Insured</p>
    <div class="credential__rule"></div>
    <p class="services">Sales • Service • and Repair of Grain Bins</p>
  </section>
</main>
</body>
</html>
```